Dorsey K. Wendell Business Card

We need a business card for our company Dorsey K. Wendell Heating & Plumbing to be distributed to potential customers. It should follow the color scheme of our logo and have a modern upscale and masculine look.

The logo is attached and the info below should also be included:

5187 W. Cedar Brook Rd.
Manheim, PA 17545

Russell T. Wendell
(717) 592-0817
russelltwendell@fernmail.net
dorseykwendell.net
PA #093148

Industry/Entity Type

Business

Contact Information for Business Card

5187 W. Cedar Brook Rd.
Manheim, PA 17545

Russell T. Wendell
(717) 592-0817
russelltwendell@fernmail.net
dorseykwendell.net
PA #093148

Colors

Designer to choose colors to be used in the design.

Requirements
Must have
• Information above included

```html
<!DOCTYPE html>
<html lang="en">
<head>
<meta charset="utf-8">
<title>Dorsey K. Wendell Business Card</title>
<link rel="stylesheet" href="https://fonts.googleapis.com/css2?family=Arimo:wght@400;700&display=swap">
<style>
  :root {
    --backdrop: #8a8b8c;
    --card-dark: #1c1c1c;
    --card-dark-mark: #2b2b2b;
    --card-light: #eeeff1;
    --brand-blue: #1b2f8e;
    --ink: #2a2a2a;
  }
  * { box-sizing: border-box; margin: 0; padding: 0; }
  html, body {
    width: 1200px; height: 781px; overflow: hidden;
    background: var(--backdrop);
    font-family: "Arimo", Arial, sans-serif;
  }
  .canvas { position: relative; width: 1200px; height: 781px; }
  .card {
    position: absolute; left: 358px; width: 453px; height: 251px;
  }
  .card--back { top: 103px; background: var(--card-dark); }
  .card--front { top: 410px; background: var(--card-light); }

  .brand {
    position: absolute; left: 0; right: 0;
    display: flex; align-items: center; justify-content: center; gap: 10px;
  }
  .card--back .brand { top: 92px; color: var(--card-dark-mark); }
  .card--front .brand { top: 44px; color: var(--brand-blue); }
  .brand__square {
    width: 52px; height: 56px; background: currentColor; flex: none;
  }
  .brand__name {
    font-weight: 700; font-size: 22px; line-height: 1.1;
    text-transform: uppercase; letter-spacing: 0.5px;
  }

  .contact {
    position: absolute; left: 0; right: 0; top: 148px;
    text-align: center; color: var(--ink);
  }
  .contact__name {
    color: var(--brand-blue); font-weight: 700; font-size: 14px;
    margin-bottom: 8px; text-transform: uppercase;
  }
  .contact__line { font-size: 11px; line-height: 14.5px; }
  .contact__label, .contact__domain { color: var(--brand-blue); font-weight: 700; }
</style>
</head>
<body>
<main class="canvas">
  <section class="card card--back" aria-label="Card back">
    <div class="brand">
      <span class="brand__square"></span>
      <span class="brand__name">Dorsey K. Wendell<br>Heating &amp; Plumbing</span>
    </div>
  </section>

  <section class="card card--front" aria-label="Card front">
    <div class="brand">
      <span class="brand__square"></span>
      <span class="brand__name">Dorsey K. Wendell<br>Heating &amp; Plumbing</span>
    </div>
    <div class="contact">
      <p class="contact__name">Russell T. Wendell</p>
      <p class="contact__line">5187 W. Cedar Brook Rd., Manheim, PA 17545</p>
      <p class="contact__line"><span class="contact__label">T:</span> (717) 592-0817 · <span class="contact__label">E:</span> russelltwendell@fernmail.net</p>
      <p class="contact__line">www.<span class="contact__domain">dorseykwendell</span>.net · PA #093148</p>
    </div>
  </section>
</main>
</body>
</html>
```